Facebook Ads for HOA Law Firm

We need to create certain ads for a Facebook ads campaign. We are a law firm in Florida that represents homeowners against HOAs. We need to create the following ads:

1. Image Ads Specifications:

File Type: JPG or PNG
Ratio: 1.91:1 to 4:5
Resolution:
a) 1:1 ratio: 1080 x 1080 pixels
b) 4:5 ratio: 1080 x 1350 pixels
Maximum File Size: 30MB
Minimum Width: 600 pixels
Minimum Height:
a) 1:1 ratio: 600 pixels
b) 4:5 ratio: 750 pixels
Key Elements to Include in the Ads:

1) Headline: "HOA Violating Your Rights?"
2) Main Message: "We sue HOAs for Homeowners."
3) Firm Name: Lindqvist Harrow, P.A.
4) Website: www.brightgatelegal-example.com
5) Phone Number: 1-800-555-0142
6) Florida Bar Compliance Statement: "Serving Homeowners in Florida with our main office in Miami-Dade."
7) Call-to-Action (CTA): Include a strong CTA such as “Contact us today for a consultation!”
8) Tone and Style: Professional yet approachable. The ad should emphasize trust, expertise, and our dedication to homeowners' rights.
9) Branding: Please use our firm's brand colors and fonts. Ensure that our logo is prominently placed within the ad.
10) Image Suggestions: Consider using images of Florida homes, frustrated homeowners, or visuals that evoke trust, protection, and legal authority.

```html
<!DOCTYPE html>
<html lang="en">
<head>
<meta charset="utf-8">
<title>Facebook Ads for HOA Law Firm</title>
<link href="https://fonts.googleapis.com/css2?family=Montserrat:wght@300;500;600;700;800&family=Oswald:wght@500&display=swap" rel="stylesheet">
<style>
  :root {
    --board: #4d4d4d;
    --board-text: #d6d6d6;
    --paper: #ffffff;
    --navy: #14149a;
    --ink: #0a0a0a;
    --band-grey: #ececef;
  }
  * { margin: 0; padding: 0; box-sizing: border-box; }
  html, body {
    width: 1200px; height: 668px; overflow: hidden;
    background: var(--board);
    font-family: "Montserrat", sans-serif;
  }
  .board { position: relative; width: 1200px; height: 668px; }
  .board-title {
    position: absolute; left: 45px; top: 28px;
    color: var(--board-text); line-height: 1.05;
  }
  .board-title .lead { font-weight: 300; font-size: 24px; display: block; }
  .board-title .strong { font-weight: 700; font-size: 25px; display: block; }
  .size-label {
    position: absolute; top: 112px;
    color: var(--board-text); font-weight: 300; font-size: 14px;
  }
  .ad { position: absolute; background: var(--paper); display: block; }
  .ad-square { left: 45px; top: 148px; width: 387px; height: 387px; }
  .ad-portrait { left: 468px; top: 148px; width: 387px; height: 484px; }
  .ad-small { left: 888px; top: 148px; width: 268px; height: 336px; }

  .headline { font-family: "Montserrat", sans-serif; font-weight: 700; fill: var(--ink); }
  .headline-accent { fill: var(--navy); font-weight: 800; }
  .message { font-family: "Montserrat", sans-serif; font-weight: 700; fill: var(--navy); }
  .message-frame { fill: none; stroke: var(--navy); }
  .firm-name { font-family: "Montserrat", sans-serif; font-weight: 700; fill: var(--navy); }
  .compliance { font-family: "Montserrat", sans-serif; font-weight: 600; fill: var(--navy); }
  .cta-pill { fill: var(--navy); }
  .cta-text { font-family: "Oswald", sans-serif; font-weight: 500; fill: var(--paper); }
  .contact { font-family: "Montserrat", sans-serif; font-weight: 700; fill: var(--paper); }
  .band-grey { fill: var(--band-grey); }
  .band-blue { fill: var(--navy); }
  .band-black { fill: var(--ink); }
  .photo-ring { fill: none; stroke: rgba(30,90,200,0.35); }
</style>
</head>
<body>
<main class="board">
  <h1 class="board-title"><span class="lead">Facebook Ads for</span><span class="strong">HOA Law Firm</span></h1>
  <span class="size-label" style="left:45px">1080x 1080</span>
  <span class="size-label" style="left:468px">1080x1350</span>
  <span class="size-label" style="left:888px">700-x-938</span>

  <svg width="0" height="0" style="position:absolute">
    <defs>
      <linearGradient id="coast" x1="0" y1="0" x2="1" y2="1">
        <stop offset="0" stop-color="#2cb5c9"/>
        <stop offset="0.45" stop-color="#3d8fb8"/>
        <stop offset="0.75" stop-color="#c94a6a"/>
        <stop offset="1" stop-color="#d83a63"/>
      </linearGradient>
      <linearGradient id="suits" x1="0" y1="0" x2="1" y2="0">
        <stop offset="0" stop-color="#1f2d55"/>
        <stop offset="0.5" stop-color="#3b4664"/>
        <stop offset="1" stop-color="#6b6f78"/>
      </linearGradient>
    </defs>
  </svg>

  <svg class="ad ad-square" viewBox="0 0 831 831">
    <clipPath id="clipSq"><rect width="831" height="831"/></clipPath>
    <g clip-path="url(#clipSq)">
      <circle cx="900" cy="-20" r="460" fill="url(#coast)" role="img" aria-label="Aerial photo of a Florida beachfront neighbourhood"/>
      <circle class="photo-ring" cx="900" cy="-20" r="440" stroke-width="40"/>
      <polygon class="band-grey" points="150,831 831,440 831,831"/>
      <rect x="388" y="442" width="425" height="300" rx="60" fill="url(#suits)" role="img" aria-label="Photo of the two firm attorneys in suits"/>
      <polygon class="band-blue" points="160,831 831,610 831,625 190,831"/>
      <polygon class="band-black" points="168,831 831,622 831,831"/>
    </g>
    <text class="headline headline-accent" x="53" y="152" font-size="76">HOA</text>
    <text class="headline" x="53" y="227" font-size="72">Violating</text>
    <text class="headline" x="53" y="297" font-size="72">Your Rights?</text>
    <rect class="message-frame" x="54" y="339" width="531" height="61" stroke-width="3"/>
    <text class="message" x="71" y="380" font-size="31" textLength="497" lengthAdjust="spacingAndGlyphs">We sue HOAs for Homeowners.</text>
    <text class="firm-name" x="53" y="512" font-size="24">Lindqvist Harrow, P.A.</text>
    <text class="compliance" font-size="26"><tspan x="53" y="600">Serving Homeowners</tspan><tspan x="53" y="630">in Florida with our main</tspan><tspan x="53" y="660">office in Miami-Dade.</tspan></text>
    <rect class="cta-pill" x="49" y="690" width="304" height="54" rx="27"/>
    <text class="cta-text" x="201" y="725" font-size="20" text-anchor="middle">Contact us today for a consultation!</text>
    <text class="contact" x="611" y="762" font-size="23" textLength="174" lengthAdjust="spacingAndGlyphs">1-800-555-0142</text>
    <text class="contact" x="436" y="795" font-size="20" textLength="349" lengthAdjust="spacingAndGlyphs">www.brightgatelegal-example.com</text>
  </svg>

  <svg class="ad ad-portrait" viewBox="0 0 831 1039">
    <clipPath id="clipPt"><rect width="831" height="1039"/></clipPath>
    <g clip-path="url(#clipPt)">
      <circle cx="880" cy="-40" r="540" fill="url(#coast)" role="img" aria-label="Aerial photo of a Florida beachfront neighbourhood"/>
      <circle class="photo-ring" cx="880" cy="-40" r="518" stroke-width="44"/>
      <polygon class="band-grey" points="150,1039 831,640 831,1039"/>
      <rect x="386" y="647" width="430" height="305" rx="60" fill="url(#suits)" role="img" aria-label="Photo of the two firm attorneys in suits"/>
      <polygon class="band-blue" points="150,1039 831,818 831,832 180,1039"/>
      <polygon class="band-black" points="160,1039 831,830 831,1039"/>
    </g>
    <text class="headline headline-accent" x="53" y="197" font-size="76">HOA</text>
    <text class="headline" x="53" y="267" font-size="72">Violating</text>
    <text class="headline" x="53" y="339" font-size="72">Your</text>
    <text class="headline" x="53" y="410" font-size="72">Rights?</text>
    <rect class="message-frame" x="52" y="465" width="531" height="62" stroke-width="3"/>
    <text class="message" x="69" y="507" font-size="31" textLength="497" lengthAdjust="spacingAndGlyphs">We sue HOAs for Homeowners.</text>
    <text class="firm-name" x="53" y="670" font-size="24">Lindqvist Harrow, P.A.</text>
    <text class="compliance" font-size="26"><tspan x="51" y="774">Serving Homeowners</tspan><tspan x="51" y="804">in Florida with our main</tspan><tspan x="51" y="834">office in Miami-Dade.</tspan></text>
    <rect class="cta-pill" x="46" y="886" width="304" height="54" rx="27"/>
    <text class="cta-text" x="198" y="921" font-size="20" text-anchor="middle">Contact us today for a consultation!</text>
    <text class="contact" x="607" y="969" font-size="23" textLength="174" lengthAdjust="spacingAndGlyphs">1-800-555-0142</text>
    <text class="contact" x="432" y="1002" font-size="20" textLength="349" lengthAdjust="spacingAndGlyphs">www.brightgatelegal-example.com</text>
  </svg>

  <svg class="ad ad-small" viewBox="0 0 577 722">
    <clipPath id="clipSm"><rect width="577" height="722"/></clipPath>
    <g clip-path="url(#clipSm)">
      <circle cx="620" cy="-30" r="385" fill="url(#coast)" role="img" aria-label="Aerial photo of a Florida beachfront neighbourhood"/>
      <circle class="photo-ring" cx="620" cy="-30" r="370" stroke-width="30"/>
      <polygon class="band-grey" points="100,722 577,445 577,722"/>
      <rect x="270" y="452" width="295" height="230" rx="45" fill="url(#suits)" role="img" aria-label="Photo of the two firm attorneys in suits"/>
      <polygon class="band-blue" points="100,722 577,566 577,578 125,722"/>
      <polygon class="band-black" points="110,722 577,577 577,722"/>
    </g>
    <text class="headline headline-accent" x="36" y="137" font-size="54">HOA</text>
    <text class="headline" x="36" y="187" font-size="50">Violating</text>
    <text class="headline" x="36" y="235" font-size="50">Your</text>
    <text class="headline" x="36" y="285" font-size="50">Rights?</text>
    <rect class="message-frame" x="35" y="323" width="370" height="43" stroke-width="2.5"/>
    <text class="message" x="48" y="352" font-size="21" textLength="345" lengthAdjust="spacingAndGlyphs">We sue HOAs for Homeowners.</text>
    <text class="firm-name" x="36" y="472" font-size="17">Lindqvist Harrow, P.A.</text>
    <text class="compliance" font-size="18"><tspan x="35" y="538">Serving Homeowners</tspan><tspan x="35" y="559">in Florida with our main</tspan><tspan x="35" y="580">office in Miami-Dade.</tspan></text>
    <rect class="cta-pill" x="32" y="615" width="211" height="39" rx="19.5"/>
    <text class="cta-text" x="137.5" y="640" font-size="13.5" text-anchor="middle">Contact us today for a consultation!</text>
    <text class="contact" x="422" y="672" font-size="16" textLength="122" lengthAdjust="spacingAndGlyphs">1-800-555-0142</text>
    <text class="contact" x="301" y="695" font-size="14" textLength="243" lengthAdjust="spacingAndGlyphs">www.brightgatelegal-example.com</text>
  </svg>
</main>
</body>
</html>
```